Meridian Rest Supply Needs Business Card

Looking for a very nice looking business card. Creative but not extravagant. We sell beds and pillows across the U.S. and need something professional but catchy. I have attached the logo.

Name : Dale Fenwick
Title : President
Phone : (800) 417-2964
Email: sleep@quorvana.com
Website: www.quorvana.com

Can be single-sided or double-sided
horizontal or vertical

Can use Blues/Greys

Target Market(s)

Mass Market

Industry/Entity Type

Retail

Contact Information for Business Card

Name : Dale Fenwick
Title : President
Phone : (800) 417-2964
Email: sleep@quorvana.com
Website: www.quorvana.com

Requirements
Must have
• Clean, Modern, Smooth
• Can use Blues/Greys
• On the other side without the information - have something simple like www.quorvana.com or our logo
Nice to have
• Surprise me
Should not have
• Nothing crazy, nothing cluttered

```html
<!DOCTYPE html>
<html lang="en">
<head>
<meta charset="utf-8">
<title>Meridian Rest Supply — Business Card</title>
<link rel="stylesheet" href="https://fonts.googleapis.com/css2?family=Questrial&display=swap">
<style>
  :root {
    --page: #ffffff;
    --card: #ffffff;
    --brand-blue: #0e96e3;
    --wordmark: #3ea6dc;
    --ink: #474747;
    --on-blue: #ffffff;
  }
  html, body {
    margin: 0;
    padding: 0;
    width: 1200px;
    height: 1162px;
    overflow: hidden;
    background: var(--page);
    font-family: "Questrial", "Century Gothic", sans-serif;
  }
  .card {
    position: absolute;
    width: 706px;
    height: 422px;
    background: var(--card);
    box-shadow: 0 1px 4px rgba(0,0,0,0.45);
    overflow: hidden;
  }
  .card--front { left: 262px; top: 152px; }
  .card--back  { left: 264px; top: 613px; width: 704px; }
  .card__art {
    position: absolute;
    inset: 0;
    width: 100%;
    height: 100%;
  }
  .wordmark {
    position: absolute;
    margin: 0;
    color: var(--wordmark);
    font-weight: 400;
    line-height: 1;
    letter-spacing: 2px;
  }
  .card--front .wordmark { left: 44px; top: 34px; font-size: 66px; }
  .card--back .wordmark {
    left: 0; right: 0; top: 148px;
    text-align: center;
    font-size: 94px;
    letter-spacing: 3px;
  }
  .holder {
    position: absolute;
    right: 178px;
    top: 184px;
    text-align: right;
    color: var(--ink);
    line-height: 1;
  }
  .holder__name { margin: 0; font-size: 52px; font-weight: 400; }
  .holder__title { margin: 8px 0 0; font-size: 26px; }
  .contact {
    position: absolute;
    left: 32px;
    top: 331px;
    margin: 0;
    padding: 0;
    list-style: none;
    color: var(--on-blue);
    font-size: 27px;
    line-height: 1;
  }
  .contact__item {
    display: flex;
    align-items: center;
    gap: 13px;
    height: 30px;
    margin-bottom: 9px;
  }
  .contact__icon { width: 30px; height: 30px; flex: none; }
  .website {
    position: absolute;
    right: 40px;
    top: 371px;
    margin: 0;
    color: var(--on-blue);
    font-size: 27px;
    line-height: 1;
  }
</style>
</head>
<body>

<section class="card card--front">
  <svg class="card__art" viewBox="0 0 882 528" preserveAspectRatio="none" aria-hidden="true">
    <path fill="var(--brand-blue)" d="M0,300 C200,372 400,416 520,414 C700,410 762,330 758,240 C754,140 722,60 684,0 L882,0 L882,528 L0,528 Z"/>
    <path fill="none" stroke="#ffffff" stroke-width="4" d="M0,297 C200,366 400,404 520,402 C690,398 748,326 744,240 C740,142 710,62 674,0"/>
  </svg>

  <h1 class="wordmark">quorvana</h1>

  <div class="holder">
    <p class="holder__name">Dale Fenwick</p>
    <p class="holder__title">President</p>
  </div>

  <ul class="contact">
    <li class="contact__item">
      <svg class="contact__icon" viewBox="0 0 30 30" aria-hidden="true">
        <circle cx="15" cy="15" r="15" fill="#fff"/>
        <path fill="var(--brand-blue)" d="M10.5 7.5 L13 10.5 L11.6 12.4 C12.6 14.6 14.4 16.6 16.8 17.8 L18.6 16.3 L21.8 18.8 L20.4 21.6 C15 22 8.6 15.4 8 10 Z"/>
      </svg>
      <span>(800) 417-2964</span>
    </li>
    <li class="contact__item">
      <svg class="contact__icon" viewBox="0 0 30 30" aria-hidden="true">
        <circle cx="15" cy="15" r="15" fill="#fff"/>
        <rect x="7.5" y="9.5" width="15" height="11" rx="1.5" fill="var(--brand-blue)"/>
        <path d="M8.5 11 L15 16 L21.5 11" fill="none" stroke="#fff" stroke-width="1.6"/>
      </svg>
      <span>sleep@quorvana.com</span>
    </li>
  </ul>

  <p class="website">www.quorvana.com</p>
</section>

<section class="card card--back">
  <svg class="card__art" viewBox="0 0 880 528" preserveAspectRatio="none" aria-hidden="true">
    <path fill="var(--brand-blue)" d="M0,400 C110,340 330,318 500,372 C600,398 680,302 745,308 C800,304 842,338 880,400 L880,528 L0,528 Z"/>
    <path fill="none" stroke="#ffffff" stroke-width="4" d="M14,398 C130,350 330,330 500,384 C602,410 680,318 745,320 C800,318 840,350 866,388"/>
  </svg>

  <p class="wordmark">quorvana</p>
</section>

</body>
</html>
```